Social responsible Renewable Energy company

We at voltaQ are an independent power producer company founded in 2021 that handles large scale deployment of Renewable Energy and carbon neutral Energy as a service model. We offer turnkey solutions using solar panel systems and this could be incorporated in our business cards. You can also find our logo in the documents provided. Another key issue is that the business cards will be printed on recicled paper, not sure if this is a limitation in deciding the design. The recycled sign should also be added on the business card and stating that the paper used was recycled. Our website is www.myvoltaq.example. It should also be very professional, not too dreamy but still needs to capture your imagination. We are really excited to get your ideas !

Target Market(s)

Renewable Energy market

Contact Information for Business Card

The business card will be printed on recycled paper. Name of the company is voltaQ. Website is www.myvoltaq.example

Requirements
Nice to have
• Our motto: Powered by renewable, driven by people.

```html
<!DOCTYPE html>
<html lang="en">
<head>
<meta charset="utf-8">
<title>voltaQ business card</title>
<link href="https://fonts.googleapis.com/css2?family=Montserrat:wght@400;500;600;700&display=swap" rel="stylesheet">
<style>
  :root {
    --backdrop: #6d6c71;
    --paper: #eceeed;
    --paper-edge: #3f6db3;
    --brand-blue: #1b8cc4;
    --ink-blue: #1d5f9e;
    --link-blue: #2aa3d6;
    --cert-green: #22a84a;
  }
  * { box-sizing: border-box; margin: 0; padding: 0; }
  html, body {
    width: 1200px;
    height: 918px;
    overflow: hidden;
    background: var(--backdrop);
    font-family: "Montserrat", sans-serif;
  }
  .sheet {
    width: 1200px;
    height: 918px;
    display: flex;
    flex-direction: column;
    align-items: center;
    justify-content: center;
    gap: 40px;
  }
  .card {
    position: relative;
    width: 700px;
    height: 400px;
    background: var(--paper);
    border-bottom: 6px solid var(--paper-edge);
    box-shadow: 0 6px 18px rgba(0, 0, 0, 0.25);
  }

  /* Front side */
  .card-front .wordmark {
    position: absolute;
    left: 0;
    right: 0;
    top: 120px;
    text-align: center;
    font-size: 112px;
    font-weight: 600;
    color: var(--brand-blue);
    letter-spacing: 2px;
    line-height: 1;
  }
  .card-front .motto {
    position: absolute;
    left: 40px;
    bottom: 34px;
    font-size: 15px;
    font-weight: 500;
    letter-spacing: 4px;
    text-transform: uppercase;
    color: var(--brand-blue);
  }

  /* Back side */
  .card-back .wordmark {
    position: absolute;
    left: 44px;
    top: 40px;
    font-size: 64px;
    font-weight: 600;
    color: var(--brand-blue);
    letter-spacing: 1px;
    line-height: 1;
  }
  .card-back .services {
    position: absolute;
    left: 44px;
    top: 140px;
    width: 600px;
    color: var(--ink-blue);
    font-weight: 700;
    font-size: 17px;
    line-height: 1.2;
    text-transform: uppercase;
  }
  .card-back .services p + p { margin-top: 10px; }
  .card-back .website {
    position: absolute;
    left: 44px;
    bottom: 42px;
    font-size: 20px;
    font-weight: 400;
    letter-spacing: 3px;
    color: var(--link-blue);
  }
  .card-back .cert-badge {
    position: absolute;
    right: 40px;
    bottom: 34px;
    width: 58px;
    height: 72px;
  }
</style>
</head>
<body>
  <main class="sheet">
    <section class="card card-front" aria-label="Card front">
      <div class="wordmark">voltaQ</div>
      <div class="motto">Powered by renewable, driven by people</div>
    </section>

    <section class="card card-back" aria-label="Card back">
      <div class="wordmark">voltaQ</div>
      <div class="services">
        <p>We handle large scale deployment of renewable energy and carbon neutral energy</p>
        <p>We offer turnkey solutions using solar panel systems</p>
      </div>
      <div class="website">www.myvoltaq.example</div>
      <svg class="cert-badge" viewBox="0 0 58 72" role="img" aria-label="Recycled paper certification badge">
        <rect x="4" y="4" width="50" height="64" rx="6" fill="none" stroke="var(--cert-green)" stroke-width="3"/>
      </svg>
    </section>
  </main>
</body>
</html>
```